Flight school sign for building, banner, and bilboard

This sign is primarily for use on the side of our flight school building to draw attention for current and future flight school students. We offer airplane and helicopter flight training, ground school training and seminars, airplane and helicopter rentals, multi-engine training, and more. I would like a professional but exciting sign that can be used across a multitude of signage options such as banners, banner ads, billboard, and other mediums so that our sign is consistent and recognizable.

Contact Information for Business Card

The business card should match our company sign somewhat but not exactly. We want good and exciting imagery or wording and energizing/exciting colors.

```html
<!DOCTYPE html>
<html lang="en">
<head>
<meta charset="utf-8">
<title>Zenith Aviation – Banner</title>
<link rel="stylesheet" href="https://fonts.googleapis.com/css2?family=Montserrat:wght@600&family=Roboto+Condensed:wght@700&family=Roboto:wght@400;500&display=swap">
<style>
  :root {
    --backdrop: #2a2a2a;
    --paper: #f4f4f6;
    --navy: #1b2545;
    --blue: #2f64ad;
    --red: #e1252f;
    --white: #ffffff;
  }
  html, body {
    margin: 0;
    width: 960px;
    height: 1200px;
    overflow: hidden;
    background: var(--backdrop);
  }
  .banner {
    position: absolute;
    left: 40px;
    top: 380px;
    width: 880px;
    height: 440px;
    background: linear-gradient(135deg, #ffffff 0%, var(--paper) 60%, #e9eaee 100%);
    overflow: hidden;
    box-shadow: 0 10px 30px rgba(0,0,0,.45);
    font-family: "Roboto", Arial, sans-serif;
  }
  .banner-shapes { position: absolute; inset: 0; }
  .brand-mark {
    position: absolute;
    left: 118px; top: 22px;
    width: 58px; height: 58px;
    border-radius: 50%;
    background: var(--navy);
  }
  .brand-name {
    position: absolute;
    left: 34px; top: 94px;
    margin: 0;
    font-family: "Montserrat", Arial, sans-serif;
    font-weight: 600;
    font-size: 21px;
    letter-spacing: .5px;
    color: var(--navy);
  }
  .brand-tagline {
    position: absolute;
    left: 48px; top: 124px;
    margin: 0;
    font-family: "Montserrat", Arial, sans-serif;
    font-weight: 600;
    font-size: 6.5px;
    letter-spacing: .6px;
    color: var(--red);
  }
  .offer-title {
    position: absolute;
    left: 32px; top: 140px;
    margin: 0;
    font-family: "Roboto Condensed", Arial, sans-serif;
    font-weight: 700;
    font-size: 30px;
    color: var(--red);
  }
  .offer-rule {
    position: absolute;
    left: 32px; top: 182px;
    width: 112px; height: 3px;
    background: var(--navy);
  }
  .service-list { margin: 0; padding: 0; list-style: none; }
  .service {
    position: absolute;
    padding-left: 24px;
    font-weight: 500;
    font-size: 14.5px;
    line-height: 17px;
    color: var(--navy);
  }
  .service::before {
    content: "";
    position: absolute;
    left: 2px; top: 3px;
    width: 11px; height: 11px;
    border-radius: 50%;
    background: var(--navy);
    box-shadow: -2px -2px 0 -1px var(--red);
  }
  .contact { margin: 0; padding: 0; list-style: none; }
  .contact-item {
    position: absolute;
    left: 34px;
    padding-left: 24px;
    color: var(--white);
    font-size: 16px;
  }
  .contact-item::before {
    content: "";
    position: absolute;
    left: 0; top: 50%;
    width: 15px; height: 15px;
    margin-top: -7.5px;
    border-radius: 50%;
    background: var(--white);
  }
  .contact-phone { top: 353px; font-size: 21px; font-weight: 500; }
  .contact-email { top: 383px; }
  .contact-web   { top: 407px; }
  .social { position: absolute; left: 272px; top: 402px; display: flex; gap: 14px; }
  .social-dot { width: 22px; height: 22px; border-radius: 50%; background: var(--white); }
</style>
</head>
<body>
  <section class="banner">
    <svg class="banner-shapes" viewBox="0 0 880 440" width="880" height="440">
      <defs>
        <linearGradient id="cockpit-tone" x1="0" y1="0" x2="0" y2="1">
          <stop offset="0" stop-color="#6d6a6e"/>
          <stop offset=".22" stop-color="#f4c98a"/>
          <stop offset=".4" stop-color="#4a4a52"/>
          <stop offset="1" stop-color="#1f2127"/>
        </linearGradient>
      </defs>
      <g role="img" aria-label="Photo: two pilots at the controls of an airliner cockpit, sunrise through the windscreen">
        <path d="M440,0 C400,80 410,250 560,330 C640,370 760,390 880,400 L880,0 Z" fill="url(#cockpit-tone)"/>
      </g>
      <path d="M420,0 C370,100 385,280 560,360 C660,405 780,425 880,430 L880,400 C760,390 640,370 560,330 C410,250 400,80 440,0 Z" fill="var(--red)"/>
      <path d="M0,440 L0,335 C120,285 260,285 380,325 C490,362 580,420 720,440 Z" fill="var(--navy)"/>
      <path d="M150,300 C260,270 360,285 440,320 C520,355 600,410 740,440 L720,440 C580,420 490,362 380,325 C300,298 220,292 150,300 Z" fill="var(--blue)"/>
      <path d="M40,325 C150,275 270,270 360,292 C250,276 150,290 40,325 Z" fill="var(--navy)"/>
    </svg>

    <div class="brand-mark"></div>
    <h1 class="brand-name">ZENITH AVIATION</h1>
    <p class="brand-tagline">LEARN TO FLY TODAY, SOAR HIGHER TOMORROW</p>

    <h2 class="offer-title">WE OFFER</h2>
    <div class="offer-rule"></div>
    <ul class="service-list">
      <li class="service" style="left:32px; top:196px;">Airplane And Helicopter<br>Flight Training</li>
      <li class="service" style="left:231px; top:194px;">Ground School Training<br>And Seminars</li>
      <li class="service" style="left:32px; top:240px;">Airplane And Helicopter<br>Rentals</li>
      <li class="service" style="left:231px; top:240px;">Multi-engine Training</li>
    </ul>

    <ul class="contact">
      <li class="contact-item contact-phone">(555) 013 0186</li>
      <li class="contact-item contact-email">info@zenithaviation.com</li>
      <li class="contact-item contact-web">www.zenithaviation.com</li>
    </ul>
    <div class="social" aria-label="Social media links">
      <span class="social-dot"></span>
      <span class="social-dot"></span>
      <span class="social-dot"></span>
      <span class="social-dot"></span>
    </div>
  </section>
</body>
</html>
```